Stationary package for Health Care company

COMPANY NAME: Vantorel.
We have a company logo. We need to create a stationary package for a new health care company. The package needs to be unique, high tech, innovative (perhaps a folded business card, or something with a die-cut). It needs to be memorable.

The company makes in-home allergy test kits - customer takes an allergy test at home (with special medical device found in the kit) then, they send in their blood samples, and the company sends back a detailed report of what they are/are not allergic to.

We need:
business cards
thank you cards
labels
stationary
envelope
9" x 12" Pocket folder

Vantorel (The company) has a brochure for the product (called Mirodane). The stationary package should compliment the brochure. The brochure will reside in the pocket folder and they must look good together. Brochure uploaded. Note: the brochure is flat. Once folded - all you will actually see in the pocket folder is the cover with the man with outstretched arms.

INFO TO BE USED ON STATIONARY: DO NOT TRY AND CONTACT THIS PERSON!

Peter J. Harwick
Chief Executive Officer
48 Orland Commerce Parkway #210
Lincolnshire IL 60071
Phone: 847-555-0172
Web site: www.vantorel-example.com
email: pharwick@vantorel-example.com
Updates

I have added all of the information to be used on the stationary package. PLEASE DO NOT TRY TO CONTACT THIS PERSON OR COMPANY. If you have any questions - contact me. Thank you. Owen

I've uploaded a cleaned up version of the Vantorel logo as a 300 dpi PSD if anyone needs it. Thank you. Owen

Target Market(s)

Doctors, hospitals, laboratories.

Industry/Entity Type

Medical

Requirements
Must have
• Must be memorable, high-tech. Must work together with Mirodane brochure. Descriptive words: freedom, breathe, clean, fresh

```html
<!DOCTYPE html>
<html lang="en">
<head>
<meta charset="utf-8">
<title>Vantorel Brochure Envelope</title>
<link href="https://fonts.googleapis.com/css2?family=PT+Sans:wght@400&display=swap" rel="stylesheet">
<style>
  :root {
    --canvas-bg: #f2f3f5;
    --brand-blue: #0b4594;
    --flap-blue: #0a3f8a;
    --paper-white: #ffffff;
    --photo-tone: #b8b98a;
  }
  html, body {
    margin: 0;
    padding: 0;
    width: 677px;
    height: 1200px;
    overflow: hidden;
    background: var(--canvas-bg);
  }
  .canvas {
    position: relative;
    width: 677px;
    height: 1200px;
  }
  .envelope-art {
    position: absolute;
    inset: 0;
    display: block;
  }
  .flap { fill: var(--flap-blue); }
  .body-blue { fill: var(--brand-blue); }
  .body-white { fill: var(--paper-white); }
  .hero-photo { fill: var(--photo-tone); }
  .hero-divider { fill: none; stroke: var(--paper-white); stroke-width: 5; }
  .brand-lockup {
    position: absolute;
    right: 40px;
    top: 1072px;
    display: flex;
    align-items: center;
    gap: 12px;
  }
  .brand-dot {
    width: 18px;
    height: 18px;
    border-radius: 50%;
    background: var(--brand-blue);
  }
  .brand-name {
    font-family: "PT Sans", sans-serif;
    font-weight: 400;
    font-size: 56px;
    line-height: 1;
    color: var(--brand-blue);
    letter-spacing: 0.5px;
  }
</style>
</head>
<body>
  <main class="canvas">
    <svg class="envelope-art" width="677" height="1200" viewBox="0 0 677 1200" xmlns="http://www.w3.org/2000/svg">
      <path class="flap" d="M90 63 H650 Q659 63 662 73 L672 199 H62 L76 73 Q79 63 90 63 Z"/>

      <rect class="body-blue" x="62" y="199" width="610" height="992"/>

      <path class="hero-photo" role="img" aria-label="Photo of a person with outstretched arms in an open field at sunrise"
            d="M62 199 H672 V615 Q430 560 62 606 Z"/>
      <path class="hero-divider" d="M62 608 Q430 560 672 618"/>

      <path class="body-white" d="M62 1100 C280 1050 480 985 672 949 V1191 H62 Z"/>
    </svg>

    <div class="brand-lockup">
      <span class="brand-dot"></span>
      <span class="brand-name">Vantorel</span>
    </div>
  </main>
</body>
</html>
```